Website Homepage for Coastal Gale Works

Website is a white label new branding of this product:
https://www.roofveldra.com

Looking for home page / landing page design.

The focus should be on its characteristics that showcase its ability to protect your roof from hurricanes and weather. Focus is only on the roof use case.

Helps restore original color
Bonds shingle granules
Penetrates and rejuvenates
Extend your roofs life
Prevents mold, mildew and moss growth
BrimGuard Colors are heat reflective and UV resistance
Environmentally Friendly
Added flexibility
Added Impact Resistance
Added Wind Resistance
Heat reflective
Reflect harmful UV rays
Reduce energy consumption
Extend the life of the shingle
Stop mold, mildew and algae from growing again!
Built it mildicide, moldicide, and algaecide.

Some other consideration marketing ideas to portray:

Roof replacement alternative with $0 down financing

Don’t replace, rejuvenate!

Stop! Before replacing your roof look at this solution…. With our advanced technology spray and seal coatings you can have a rejuvenated roof that is better than a new one! At a fraction of the cost!

Repel wind, repel water and repel impact. Make your roof stronger than ever.

Is your roof ready for hurricane season? What if there was a simple 1 day application coating that could help you to strengthen your roof against wind, rain and impact?

Self insured home? Protect your roof with our rejuvenating roof coatings that extend the life of your roof by 15+ years.

Have you recently installed a roof? Don’t wait for the next hurricane to damage it. Protect it today with our sealant coatings that repel wind, water and impact!

Ready for a new roof but don’t have the budget. Use our colored coatings that not only make your roof new again, but can also recolor it!

The sun is damaging your roof every day! Our coatings protect it from UV damage as well as water, wind, and impact!

Have a tile or clay roof? Tired of algae, mold and mildew growing on your roof? We will clean your roof and prevent regrowth in the future with our coatings!

Industry/Entity Type

Construction

Number of Pages Required

1 page

Font styles to use
Sans Serif

Colors
0054AA
0677BA
7BADD7
CADEEF
E8F1F8
0094D4
00A9DD
6FCCEA
C7EBF8
E9F6FB

Requirements
Nice to have
• Modern blue / grey / black color scheme. Not a lot of white space.

```html
<!DOCTYPE html>
<html lang="en">
<head>
<meta charset="utf-8">
<title>Coastal Gale Works – Protect Your Roof From Hurricanes</title>
<link href="https://fonts.googleapis.com/css2?family=Poppins:wght@400;500;600&family=Jost:wght@400;500&display=swap" rel="stylesheet">
<style>
:root{
  --navy:#1b1846;
  --navy-deep:#15123b;
  --blue:#0a8ef0;
  --blue-strong:#0677ba;
  --sky:#c7ebf8;
  --ink:#2b2b33;
  --muted:#55555f;
  --field:#e9ecf2;
  --white:#ffffff;
  --press:#1c3d7a;
  --badge:#b9c4d2;
}
*{box-sizing:border-box;margin:0;padding:0}
html,body{width:1200px;height:4311px;overflow:hidden}
body{position:relative;background:var(--white);font-family:"Jost",sans-serif;color:var(--ink)}
a{text-decoration:none}
.abs{position:absolute}
.heading{font-family:"Poppins",sans-serif;font-weight:500;text-transform:uppercase}
.pill{position:absolute;display:flex;align-items:center;justify-content:center;border-radius:40px;font-family:"Poppins",sans-serif;font-size:19px;text-transform:uppercase;color:var(--white);background:var(--blue);white-space:nowrap}
.photo{position:absolute;overflow:hidden}

/* Header */
.site-header{position:absolute;left:0;top:0;width:1200px;height:92px;background:var(--navy)}
.brand{position:absolute;font-family:"Poppins",sans-serif;font-weight:600;color:var(--white);letter-spacing:1px;line-height:1.1;white-space:nowrap}
.nav{position:absolute;left:0;top:0;width:1200px;height:92px}
.nav a{position:absolute;top:35px;font-family:"Poppins",sans-serif;font-size:19px;line-height:24px;color:var(--white);white-space:nowrap}

/* Hero */
.hero{position:absolute;left:0;top:92px;width:1200px;height:641px;background:var(--navy)}
.hero-title{position:absolute;left:47px;top:84px;font-size:44px;line-height:54px;color:var(--white);font-weight:600}
.hero-sub{position:absolute;left:47px;top:253px;font-family:"Poppins",sans-serif;font-size:20px;line-height:25px;color:var(--white);text-transform:uppercase}
.feature{position:absolute;width:110px;text-align:left;color:var(--white);font-family:"Poppins",sans-serif;font-size:14px}
.feature svg{display:block;margin-bottom:6px}

.quote-bar{position:absolute;left:112px;width:969px;height:117px;border-radius:60px;background:var(--blue)}
.field{position:absolute;top:37px;width:150px;height:50px;border-radius:25px;background:var(--field);font-family:"Poppins",sans-serif;font-size:15px;color:#6b6f7a;padding-left:27px;display:flex;align-items:center}

/* Services */
.section-title{position:absolute;left:0;width:1200px;text-align:center;font-size:36px;color:var(--ink)}
.service-label{font-size:18px;padding:0 28px;height:40px}

/* Hurricane */
.hurricane{position:absolute;left:0;top:1595px;width:1200px;height:516px;background:var(--navy)}
.copy{font-family:"Jost",sans-serif;font-size:16px;line-height:22px;color:#dcdcf0}

/* Benefits */
.benefit-list{position:absolute;left:110px;top:2410px;list-style:none}
.benefit-list li{display:flex;align-items:center;height:56.6px;font-size:18px;color:var(--muted)}
.benefit-list svg{margin-right:12px;flex:none}

/* Recent work */
.recent{position:absolute;left:0;top:2903px;width:1200px;height:681px;background:var(--navy)}

/* Press */
.press-badge{position:absolute;top:3728px;height:70px;border-radius:12px;background:var(--badge)}

/* Footer */
.site-footer{position:absolute;left:12px;top:3884px;width:1188px;height:427px;background:var(--navy)}
.foot-col{position:absolute;top:88px}
.foot-col h4{font-family:"Poppins",sans-serif;font-weight:500;font-size:21px;color:var(--blue);margin-bottom:14px;white-space:nowrap}
.foot-col a{display:block;font-family:"Poppins",sans-serif;font-size:15px;color:var(--white);height:44.7px;text-transform:uppercase;white-space:nowrap}
.foot-col a::before{content:"›";color:var(--blue);margin-right:8px}
.contact{position:absolute;left:55px;display:flex;gap:14px;color:var(--white);font-family:"Poppins",sans-serif;font-size:16px;line-height:19px}
.divider{position:absolute;left:43px;top:361px;width:1108px;height:1px;background:#3c4a9a}
.legal{position:absolute;top:394px;font-family:"Poppins",sans-serif;font-size:12px;font-weight:500;color:var(--white)}
</style>
</head>
<body>

<header class="site-header">
  <div class="brand" style="left:37px;top:24px;font-size:19px">COASTAL GALE<br>WORKS</div>
  <nav class="nav">
    <a style="left:275px" href="#">HOME</a>
    <a style="left:375px" href="#">ABOUT</a>
    <a style="left:490px" href="#">SERVICES</a>
    <a style="left:627px" href="#">GALLERY</a>
    <a style="left:758px" href="#">TESTIMONIALS</a>
  </nav>
  <a class="pill" style="left:956px;top:27px;width:194px;height:41px" href="#">Get a Quote</a>
</header>

<section class="hero">
  <div class="photo" role="img" aria-label="Worker in a safety harness spraying sealer coating on a shingle roof with trees behind"
       style="left:0;top:0;width:1200px;height:641px;clip-path:polygon(762px 0,1200px 0,1200px 641px,620px 641px);background:linear-gradient(160deg,#5f8a3c 0%,#7b8f5c 30%,#8d8a86 55%,#6f6c6c 100%)"></div>
  <h1 class="heading hero-title">Protect Your Roof<br>From Hurricanes<br>And Weather</h1>
  <p class="hero-sub">Transform your home with a roof that<br>withstands any storm</p>
  <a class="pill" style="left:47px;top:328px;width:194px;height:43px" href="#">Get a Quote</a>

  <div class="feature" style="left:50px;top:427px">
    <svg width="68" height="56" viewBox="0 0 68 56" fill="none" stroke="#4da3ff" stroke-width="2"><path d="M8 30 L34 10 L60 30"/><rect x="14" y="28" width="40" height="24"/><path d="M2 20h18M4 26h12M46 16h18M50 22h14"/></svg>
    Repel Wind
  </div>
  <div class="feature" style="left:189px;top:420px">
    <svg width="68" height="62" viewBox="0 0 68 62" fill="none" stroke="#4da3ff" stroke-width="2"><path d="M22 14a12 8 0 0 1 24 0"/><path d="M26 20v6M34 20v8M42 20v6"/><path d="M6 50 L34 30 L62 50"/><rect x="14" y="46" width="40" height="14"/></svg>
    Repel Water
  </div>
  <div class="feature" style="left:340px;top:422px">
    <svg width="68" height="60" viewBox="0 0 68 60" fill="none" stroke="#4da3ff" stroke-width="2"><circle cx="16" cy="14" r="9"/><path d="M12 14l4 4 6-8"/><path d="M10 56 L40 22 L64 56 Z"/><path d="M22 44h32M30 34h18"/></svg>
    Repel Impact
  </div>

  <form class="quote-bar" style="top:579px">
    <div class="field" style="left:39px">NAME</div>
    <div class="field" style="left:214px">EMAIL</div>
    <div class="field" style="left:394px">PHONE</div>
    <div class="field" style="left:573px">ADDRESS</div>
    <button class="pill" type="button" style="left:747px;top:37px;width:194px;height:50px;border:0;background:var(--navy-deep)">Get a Quote</button>
  </form>
</section>

<h2 class="heading section-title" style="top:875px">How We Can Serve You</h2>

<div class="photo" role="img" aria-label="Front of a house with a dark shingle roof, white siding and garage" style="left:89px;top:963px;width:477px;height:477px;border-radius:50px;background:linear-gradient(180deg,#9fb7cf 0%,#c5d0da 38%,#4c5663 48%,#cfcfc8 62%,#6f8c57 100%)"></div>
<span class="pill service-label" style="left:197px;top:1194px">Residential Roofing</span>

<div class="photo" role="img" aria-label="Worker spraying a commercial shingle roof" style="left:591px;top:963px;width:519px;height:232px;border-radius:50px;background:linear-gradient(135deg,#cfd2d6 0%,#9ea3a8 50%,#6b6e72 100%)"></div>
<span class="pill service-label" style="left:809px;top:1081px">Commercial Roofing</span>

<div class="photo" role="img" aria-label="Coated grey shingle roof of a house under a cloudy sky" style="left:591px;top:1215px;width:519px;height:225px;border-radius:50px;background:linear-gradient(180deg,#a9bed1 0%,#5b6674 40%,#4b5562 70%,#d8d8d2 100%)"></div>
<span class="pill service-label" style="left:814px;top:1285px;width:250px">Roof Coating</span>

<a class="pill" style="left:482px;top:1488px;width:219px;height:45px;background:var(--navy);font-size:18px" href="#">View All Services</a>

<section class="hurricane">
  <svg class="abs" style="left:0;top:0" width="520" height="516" role="img" aria-label="Aerial view of a worker coating a shingle roof beside a green lawn">
    <defs><linearGradient id="roofShot" x1="0" y1="0" x2="1" y2="1"><stop offset="0" stop-color="#6f8d4e"/><stop offset="0.45" stop-color="#7e7a76"/><stop offset="1" stop-color="#5d5a58"/></linearGradient></defs>
    <path d="M0 0 H250 L492 180 Q510 195 495 215 L170 516 H0 Z" fill="url(#roofShot)"/>
  </svg>
  <h2 class="heading abs" style="left:598px;top:114px;font-size:35px;line-height:43px;color:var(--white)">Is Your Roof Ready For<br>Hurricane Season?.</h2>
  <p class="copy abs" style="left:604px;top:228px;width:510px">What if there was a simple 1 day application coating that could help you to strengthen your roof against wind, rain and impact. The sun is damaging your roof every day! Our coatings protect it from UV damage as well as water, wind, and impact!</p>
  <a class="pill" style="left:606px;top:358px;width:194px;height:46px" href="#">Get a Quote</a>
</section>

<h2 class="heading abs" style="left:110px;top:2276px;font-size:30px;line-height:35px;color:var(--ink)">Our Coatings Protect It<br>From UV Damage As Well<br>As Water, Wind, And Impact!</h2>
<ul class="benefit-list">
  <li><svg width="42" height="42" viewBox="0 0 42 42"><circle cx="21" cy="21" r="21" fill="#0a8ef0"/><path d="M12 22l6 6 12-13" stroke="#fff" stroke-width="4" fill="none"/></svg>Helps restore original color</li>
  <li><svg width="42" height="42" viewBox="0 0 42 42"><circle cx="21" cy="21" r="21" fill="#0a8ef0"/><path d="M12 22l6 6 12-13" stroke="#fff" stroke-width="4" fill="none"/></svg>Bonds shingle granules</li>
  <li><svg width="42" height="42" viewBox="0 0 42 42"><circle cx="21" cy="21" r="21" fill="#0a8ef0"/><path d="M12 22l6 6 12-13" stroke="#fff" stroke-width="4" fill="none"/></svg>Penetrates and rejuvenates</li>
  <li><svg width="42" height="42" viewBox="0 0 42 42"><circle cx="21" cy="21" r="21" fill="#0a8ef0"/><path d="M12 22l6 6 12-13" stroke="#fff" stroke-width="4" fill="none"/></svg>Prevents mold, mildew and moss growth</li>
  <li><svg width="42" height="42" viewBox="0 0 42 42"><circle cx="21" cy="21" r="21" fill="#0a8ef0"/><path d="M12 22l6 6 12-13" stroke="#fff" stroke-width="4" fill="none"/></svg>BrimGuard Colors are heat reflective and UV resistance</li>
  <li><svg width="42" height="42" viewBox="0 0 42 42"><circle cx="21" cy="21" r="21" fill="#0a8ef0"/><path d="M12 22l6 6 12-13" stroke="#fff" stroke-width="4" fill="none"/></svg>Environmentally Friendly</li>
  <li><svg width="42" height="42" viewBox="0 0 42 42"><circle cx="21" cy="21" r="21" fill="#0a8ef0"/><path d="M12 22l6 6 12-13" stroke="#fff" stroke-width="4" fill="none"/></svg>Stop mold, mildew and algae from growing again!</li>
</ul>
<div class="photo" role="img" aria-label="Worker in hard hat and safety harness seen from behind on a roof" style="left:634px;top:2267px;width:451px;height:554px;border-radius:60px;background:linear-gradient(180deg,#8e9aa2 0%,#dfe3e6 35%,#c8b169 55%,#3d5680 80%,#6f8a7a 100%)"></div>

<section class="recent">
  <h2 class="heading section-title" style="top:50px;font-size:30px;color:var(--white)">Our Recent Work</h2>
  <div class="photo" role="img" aria-label="Finished house roof with garage" style="left:142px;top:127px;width:491px;height:206px;border-radius:40px;background:linear-gradient(180deg,#a7bccf 0%,#4c5663 40%,#d3d3cc 70%,#7e8c5c 100%)"></div>
  <div class="photo" role="img" aria-label="Long coated shingle roof beside trees" style="left:646px;top:127px;width:412px;height:206px;border-radius:40px;background:linear-gradient(180deg,#b8c6d4 0%,#5e8a45 35%,#807b77 60%,#5d5a58 100%)"></div>
  <div class="photo" role="img" aria-label="Worker in harness on a metal roof" style="left:142px;top:348px;width:295px;height:208px;border-radius:40px;background:linear-gradient(160deg,#7f8d74 0%,#e2e4e6 45%,#3f5a86 75%,#6f8a7a 100%)"></div>
  <div class="photo" role="img" aria-label="Worker spraying coating on shingles" style="left:452px;top:348px;width:295px;height:208px;border-radius:40px;background:linear-gradient(135deg,#a6a9ad 0%,#77797c 60%,#56585b 100%)"></div>
  <div class="photo" role="img" aria-label="Worker coating a roof near evergreen trees" style="left:763px;top:348px;width:295px;height:208px;border-radius:40px;background:linear-gradient(160deg,#5d8a3f 0%,#6e8a58 40%,#8a8682 70%,#66625f 100%)"></div>
</section>

<h2 class="heading section-title" style="top:3637px;font-size:24px;color:var(--press)">As Seen On?</h2>
<div class="press-badge" style="left:126px;width:147px" role="img" aria-label="Media listing badge"></div>
<div class="press-badge" style="left:321px;width:146px" role="img" aria-label="Media listing badge"></div>
<div class="press-badge" style="left:511px;width:147px" role="img" aria-label="Media listing badge"></div>
<div class="press-badge" style="left:703px;width:147px" role="img" aria-label="Media listing badge"></div>
<div class="press-badge" style="left:897px;width:141px" role="img" aria-label="Media listing badge"></div>

<footer class="site-footer">
  <div class="brand" style="left:67px;top:80px;font-size:21px">COASTAL GALE<br>WORKS</div>
  <div class="contact" style="top:186px">
    <svg width="22" height="22" viewBox="0 0 24 24" fill="#0a8ef0"><path d="M6.6 10.8a15 15 0 0 0 6.6 6.6l2.2-2.2a1 1 0 0 1 1-.25 11.4 11.4 0 0 0 3.6.57 1 1 0 0 1 1 1V20a1 1 0 0 1-1 1A17 17 0 0 1 3 4a1 1 0 0 1 1-1h3.5a1 1 0 0 1 1 1c0 1.25.2 2.45.57 3.6a1 1 0 0 1-.25 1z"/></svg>
    <span>(800) 555-0142</span>
  </div>
  <div class="contact" style="top:229px">
    <svg width="22" height="28" viewBox="0 0 24 30" fill="#0a8ef0"><path d="M12 0a10 10 0 0 0-10 10c0 7.5 10 20 10 20s10-12.5 10-20A10 10 0 0 0 12 0zm0 14a4 4 0 1 1 0-8 4 4 0 0 1 0 8z"/></svg>
    <span>2250 Harbor Point Road,<br>Suite 210 Tampa, Florida<br>33602 United States</span>
  </div>

  <div class="foot-col" style="left:368px">
    <h4>SEALERS</h4>
    <a href="#">Roof Sealers</a><a href="#">Roof Coatings</a><a href="#">Energy Efficient Roof</a><a href="#">Roof Facts</a>
  </div>
  <div class="foot-col" style="left:663px">
    <h4>COMPANY</h4>
    <a href="#">Home</a><a href="#">About</a><a href="#">Gallery</a><a href="#">Contact</a>
  </div>
  <div class="foot-col" style="left:884px">
    <h4>COASTAL GALE WORKS</h4>
    <a href="#">FAQs</a><a href="#">Test Videos</a><a href="#">Video Gallery</a><a href="#">Get a Quote</a>
  </div>

  <div class="divider"></div>
  <p class="legal" style="left:43px">© ALL RIGHTS RESERVED BY COASTAL GALE WORKS</p>
  <p class="legal" style="right:25px">PRIVACY POLICY | TERM AND CONDITIONS</p>
</footer>

</body>
</html>
```